Business card for exciting VC company

Should look simple, crisp, and modern.

Industry/Entity Type

Venture Capital

Contact Information for Business Card

Would like to see at least one design that has our blue on the back with the tagline "Transforming Traditional Industry" and white front with contact details.

Font styles to use
Sans Serif

Requirements
Must have
• Logo

Darius Pellworth
dpellworth@brindlegate.vc
Managing Partner
M (628)304-xxxx

```html
<!DOCTYPE html>
<html lang="en">
<head>
<meta charset="utf-8">
<title>Brindlegate Capital — Business Card</title>
<link href="https://fonts.googleapis.com/css2?family=Lato:wght@400;700&display=swap" rel="stylesheet">
<style>
  :root {
    --ink: #050505;
    --paper: #ffffff;
    --brand-blue: #3f7fc6;
    --text-dark: #151515;
    --stage: #e9e7e4;
  }
  * { box-sizing: border-box; margin: 0; padding: 0; }
  html, body { width: 1200px; height: 900px; overflow: hidden; }
  body {
    background: var(--stage);
    font-family: "Lato", Arial, sans-serif;
    position: relative;
  }
  .card {
    position: absolute;
    left: 290px;
    width: 620px;
    height: 354px;
    box-shadow: 0 6px 18px rgba(0,0,0,0.18);
    overflow: hidden;
  }
  .card-back { top: 60px; background: var(--ink); }
  .card-front { top: 476px; background: var(--paper); }

  .wordmark {
    position: absolute;
    font-weight: 700;
    letter-spacing: 0.14em;
    text-transform: uppercase;
    white-space: nowrap;
  }
  .card-back .wordmark {
    color: var(--paper);
    font-size: 34px;
    left: 0; right: 0; top: 118px;
    text-align: center;
  }
  .tagline {
    position: absolute;
    left: 0; right: 0; top: 280px;
    text-align: center;
    color: var(--brand-blue);
    font-size: 15px;
    letter-spacing: 0.02em;
    text-transform: uppercase;
  }

  .card-front .wordmark {
    color: var(--text-dark);
    font-size: 21px;
    right: 34px; top: 50px;
  }
  .swoosh { position: absolute; inset: 0; width: 620px; height: 354px; }
  .holder { position: absolute; left: 40px; top: 46px; }
  .holder-name {
    color: var(--brand-blue);
    font-weight: 700;
    font-size: 20px;
    text-transform: uppercase;
    letter-spacing: 0.01em;
  }
  .holder-title { color: var(--text-dark); font-size: 17px; margin-top: 2px; }

  .contact-list { position: absolute; left: 40px; top: 186px; list-style: none; }
  .contact-list li {
    display: flex; align-items: center; gap: 12px;
    color: var(--text-dark); font-size: 17px; line-height: 26px;
  }
  .contact-list svg { width: 18px; height: 18px; flex: none; }

  .website {
    position: absolute; right: 40px; bottom: 66px;
    color: var(--paper); font-size: 15px;
  }
  .website .domain { color: var(--brand-blue); }
</style>
</head>
<body>
  <section class="card card-back" aria-label="Card back">
    <div class="wordmark">Brindlegate Capital</div>
    <p class="tagline">Transforming Traditional Industry</p>
  </section>

  <section class="card card-front" aria-label="Card front">
    <svg class="swoosh" viewBox="0 0 620 354" aria-hidden="true">
      <path d="M0 300 C180 300 330 250 470 160 C530 125 580 105 620 98 L620 354 L0 354 Z" fill="var(--brand-blue)"/>
      <path d="M0 322 C190 318 330 262 460 185 C530 145 580 120 620 110 L620 354 L0 354 Z" fill="var(--paper)"/>
      <path d="M0 328 C200 324 340 268 470 188 C535 150 585 125 620 116 L620 354 L0 354 Z" fill="var(--ink)"/>
    </svg>

    <div class="holder">
      <h1 class="holder-name">Darius Pellworth</h1>
      <p class="holder-title">Managing Partner</p>
    </div>

    <div class="wordmark">Brindlegate Capital</div>

    <ul class="contact-list">
      <li>
        <svg viewBox="0 0 24 24" aria-hidden="true"><path fill="var(--brand-blue)" d="M6.6 10.8a15.1 15.1 0 0 0 6.6 6.6l2.2-2.2a1 1 0 0 1 1-.25 11.4 11.4 0 0 0 3.6.57 1 1 0 0 1 1 1V20a1 1 0 0 1-1 1A17 17 0 0 1 3 4a1 1 0 0 1 1-1h3.5a1 1 0 0 1 1 1c0 1.25.2 2.45.57 3.57a1 1 0 0 1-.25 1z"/></svg>
        <span>(628)304-xxxx</span>
      </li>
      <li>
        <svg viewBox="0 0 24 24" aria-hidden="true"><rect x="2" y="5" width="20" height="14" fill="var(--brand-blue)"/><path d="M2 5l10 8 10-8" fill="none" stroke="var(--paper)" stroke-width="1.6"/></svg>
        <span>dpellworth@brindlegate.vc</span>
      </li>
    </ul>

    <p class="website">www.<span class="domain">brindlegate</span>.vc</p>
  </section>
</body>
</html>
```